Responsive, beautiful email sign-up process pages

My client wants to re-imagine their email newsletter sign up process. The funnel currently starts in the first panel of their home page carousel at:

https://thriftbeacon.co.uk/

It is also featured in the right side of the footer.

I would like to start, what could become a full template re-design project by optimising this crucial user journey. I am attaching the screenshots from the current user journey below and it would be great to get some designs that improve on the look and feel.

Thank you,
Dorian

Target Market(s)

People who want to maximise the interest rate they receive on their cash savings.

Industry/Entity Type

Financial Service

Coding

Coded - Design and coding required

Number of Pages Required

4 page

Font styles to use
Sans Serif

Requirements
Must have
• A well designed, responsive design for all of the elements of the user journey funnel that works well on desktop, laptop, tablet and phone. The site is currently using Bootstrap 3.* for the responsive templates, so it would be useful to continue leveraging these libraries, but in a much more visually appealing way.
• It is felt that the current overall site is dull and unprofessional, so we are using this as a way of showing how much better it could be, which should lead to a sitewide "facelift".
Nice to have
• Creative use of css, svg and javascript to optimise the user experience on all target platforms.
Should not have
• Non-responsive designs.

```html
<!DOCTYPE html>
<html lang="en">
<head>
<meta charset="utf-8">
<title>Thrift Beacon – Home</title>
<link href="https://fonts.googleapis.com/css2?family=Open+Sans:wght@400;600;700;800&display=swap" rel="stylesheet">
<style>
:root{
  --orange:#f07c1e;
  --nav:#3a3a3a;
  --ink:#333;
  --muted:#777;
  --light:#f2f2f2;
  --line:#ddd;
  --footer-bg:#f7f7f7;
  --footer-bar:#2b2b2b;
}
*{box-sizing:border-box;margin:0;padding:0}
html,body{width:759px;height:1200px;overflow:hidden;background:#fff}
body{font-family:"Open Sans",Arial,sans-serif;color:var(--ink);position:relative}
.header{height:78px;position:relative}
.brand{position:absolute;left:22px;top:22px;display:flex;align-items:center;gap:7px}
.brand-mark{width:26px;height:26px;border-radius:50%;background:var(--orange)}
.brand-name{font-size:17px;font-weight:700;color:#555;line-height:1;white-space:nowrap}
.brand-name small{display:block;font-size:9px;font-weight:700;color:#555;margin-top:2px}
.expert{position:absolute;left:300px;top:22px;display:flex;align-items:center;gap:8px}
.expert svg{width:24px;height:24px}
.expert p{font-size:8px;color:var(--muted);white-space:nowrap}
.expert strong{display:block;font-size:15px;color:var(--orange);font-weight:700}
.top-actions{position:absolute;right:18px;top:12px;display:flex;gap:4px}
.top-actions span{background:var(--orange);color:#fff;font-size:7px;font-weight:700;padding:4px 8px;text-transform:uppercase}
.top-actions span.dark{background:#555}
.nav{position:absolute;top:78px;left:0;width:759px;height:22px;background:var(--nav);display:flex;padding-left:12px}
.nav a{color:#ddd;font-size:7.5px;text-decoration:none;padding:0 9px;line-height:22px;white-space:nowrap}
.nav a.active{background:var(--orange);color:#fff}
.hero{position:absolute;top:100px;left:0;width:759px;height:346px;background:linear-gradient(120deg,#5b6e4a 0%,#9aa37a 40%,#c7c19a 70%,#8a8f6a 100%)}
.hero-panel{position:absolute;left:48px;top:62px;width:268px;height:226px;background:rgba(30,30,30,.72);padding:18px}
.hero-panel h1{color:#fff;font-size:27px;font-weight:800;line-height:1}
.hero-panel h2{color:#fff;font-size:12px;font-weight:700;margin-top:5px;white-space:nowrap}
.hero-panel ul{list-style:none;margin-top:12px}
.hero-panel li{color:#fff;font-size:10px;display:flex;align-items:center;gap:7px;margin-bottom:6px;white-space:nowrap}
.hero-panel li svg{width:11px;height:11px;flex:none}
.email-input{margin-top:10px;background:#fff;height:22px;width:160px;font-size:8px;color:#999;padding:5px 8px}
.cta{display:inline-block;margin-top:8px;background:var(--orange);color:#fff;font-size:8px;font-weight:700;padding:6px 10px;text-transform:uppercase;white-space:nowrap}
.hero-arrow{position:absolute;top:160px;width:20px;height:26px}
.tabs{position:absolute;top:446px;left:0;width:759px;height:22px;display:flex;justify-content:center;gap:2px;background:#eee}
.tabs span{width:150px;text-align:center;line-height:22px;font-size:7.5px;font-weight:700;color:#fff;background:#8d8d8d;text-transform:uppercase;white-space:nowrap}
.tabs span.active{background:var(--orange)}
.section-title{position:absolute;left:0;width:759px;text-align:center;color:var(--orange);font-size:15px;font-weight:600}
.offers{position:absolute;top:518px;left:88px;display:flex;gap:14px}
.offer{width:184px;height:132px;background:var(--light);border-top:3px solid var(--orange);text-align:center;padding:12px 10px}
.offer h3{font-size:12.5px;font-weight:600;color:var(--ink);white-space:nowrap}
.offer p{font-size:7px;color:var(--muted);margin-top:10px;line-height:1.5;height:32px}
.offer .btn{display:inline-block;margin-top:10px;font-size:7px;color:var(--muted);border:1px solid #ccc;background:#fff;padding:3px 8px;white-space:nowrap}
.quotes{position:absolute;top:698px;left:88px;display:flex;gap:14px}
.quote{width:284px;height:130px;border:1px solid var(--line);padding:12px 14px;font-size:8px;line-height:1.5;color:#555}
.quote cite{display:block;margin-top:8px;font-weight:700;font-style:normal;color:var(--ink)}
.press{position:absolute;top:858px;left:0;width:759px;height:50px;display:flex;align-items:center;justify-content:center;gap:12px;border-top:1px solid var(--line);border-bottom:1px solid var(--line)}
.press .badge{width:60px;height:30px;background:#cfcfcf}
.press .badge.round{width:30px;border-radius:50%;background:#555}
.press .badge.square{width:30px;background:#888}
.press svg{width:10px;height:16px}
.callbar{position:absolute;top:932px;left:0;width:759px;height:32px;background:var(--orange);color:#fff;display:flex;align-items:center;padding-left:58px;gap:20px}
.callbar span{font-size:9px;font-weight:700;text-transform:uppercase}
.callbar strong{font-size:16px;font-weight:700}
.footer{position:absolute;top:964px;left:0;width:759px;height:186px;background:var(--footer-bg);display:flex;align-items:flex-start;padding:16px 58px;gap:26px}
.footer h4{font-size:8px;color:var(--orange);font-weight:700;margin-bottom:6px;line-height:1.4}
.footer p,.footer li{font-size:7px;color:#666;line-height:1.6;list-style:none}
.col-intro{width:140px}
.col-links{width:84px}
.signup{width:170px;background:#fff;border:1px solid var(--line);padding:10px}
.signup .field{height:18px;border:1px solid #ccc;font-size:7px;color:#999;padding:0 0 0 6px;margin-top:8px;display:flex;justify-content:space-between;align-items:center}
.signup .go{background:var(--orange);color:#fff;font-size:7px;font-weight:700;padding:0 8px;line-height:16px}
.bottom{position:absolute;top:1150px;left:0;width:759px;height:50px;background:var(--footer-bar);padding:14px 58px;color:#aaa;font-size:7px;line-height:1.7}
</style>
</head>
<body>
<header class="header">
  <div class="brand"><span class="brand-mark"></span><span class="brand-name">Thrift Beacon<small>thriftbeacon.co.uk</small></span></div>
  <div class="expert">
    <svg viewBox="0 0 24 24"><circle cx="12" cy="12" r="12" fill="#f07c1e"/><path d="M8 6l3 0 1 4-2 1a8 8 0 004 4l1-2 4 1v3c-6 1-12-5-11-11z" fill="#fff"/></svg>
    <p>Speak Direct to a Savings Expert<strong>0800 555 0142</strong></p>
  </div>
  <div class="top-actions"><span>Alert</span><span>Register Now</span><span class="dark">Login</span></div>
</header>
<nav class="nav">
  <a class="active">Home</a><a>Concierge Service</a><a>Best Buy Tables</a><a>Rate Tracker</a><a>News and Alerts</a><a>Advice and Guides</a><a>Awards</a><a>Testimonials</a><a>About Us</a><a>Contact Us</a>
</nav>
<section class="hero" role="img" aria-label="Photo of a family walking together outdoors in sunshine">
  <svg class="hero-arrow" style="left:10px" viewBox="0 0 20 26"><path d="M14 3L5 13l9 10" stroke="#fff" stroke-width="3" fill="none"/></svg>
  <svg class="hero-arrow" style="right:10px" viewBox="0 0 20 26"><path d="M6 3l9 10-9 10" stroke="#fff" stroke-width="3" fill="none"/></svg>
  <div class="hero-panel">
    <h1>GET FREE</h1>
    <h2>WHOLE OF MARKET INFORMATION</h2>
    <ul>
      <li><svg viewBox="0 0 12 12"><path d="M1 6l3 3 7-7" stroke="#f07c1e" stroke-width="2.2" fill="none"/></svg>Uncompromised Best Buy Tables</li>
      <li><svg viewBox="0 0 12 12"><path d="M1 6l3 3 7-7" stroke="#f07c1e" stroke-width="2.2" fill="none"/></svg>Account Monitoring and Alert Services</li>
      <li><svg viewBox="0 0 12 12"><path d="M1 6l3 3 7-7" stroke="#f07c1e" stroke-width="2.2" fill="none"/></svg>Access to Savings Experts</li>
    </ul>
    <div class="email-input">Email Address</div>
    <span class="cta">Choose your free services ›</span>
  </div>
</section>
<div class="tabs"><span class="active">Free Information</span><span>Inheritance Tax</span><span>Over £100,000 in Savings</span></div>

<h2 class="section-title" style="top:490px">Specialist Advice</h2>
<div class="offers">
  <div class="offer"><h3>£100,000 plus in savings?</h3><p>Find out how our dedicated team can help you spread larger balances across safe accounts.</p><span class="btn">Would you like to know more?</span></div>
  <div class="offer"><h3>Wealth Management</h3><p>Speak with our partner advisers about investments and long term planning.</p><span class="btn">Would you like to know more?</span></div>
  <div class="offer"><h3>Take Our £50 Challenge</h3><p>See how much more interest you could earn in just a few minutes.</p><span class="btn">Would you like to know more?</span></div>
</div>

<h2 class="section-title" style="top:670px">Thrift Beacon in the Press</h2>
<div class="quotes">
  <blockquote class="quote">"Thrift Beacon is a very useful free service that keeps savers on top of the best rates and warns them when their rate drops. Members get clear tables and timely alerts."<cite>— Jane Holt, Savings Writer</cite></blockquote>
  <blockquote class="quote">"A great site for anyone who wants better returns on cash without the stress of checking every bank by hand. Friendly, fair and independent."<cite>— Tom Reed, Money Editor</cite></blockquote>
</div>

<div class="press">
  <svg viewBox="0 0 10 16"><path d="M8 2L2 8l6 6" stroke="#999" stroke-width="2" fill="none"/></svg>
  <span class="badge"></span><span class="badge"></span><span class="badge"></span><span class="badge"></span><span class="badge round"></span><span class="badge round"></span><span class="badge square"></span><span class="badge"></span>
  <svg viewBox="0 0 10 16"><path d="M2 2l6 6-6 6" stroke="#999" stroke-width="2" fill="none"/></svg>
</div>

<div class="callbar"><span>Questions? Call us on</span><strong>0800 555 0142</strong></div>

<footer class="footer">
  <div class="col-intro"><h4>You're searching for a better deal for savers</h4><p>Thrift Beacon members receive free best buy tables, rate alerts and expert news every month.</p></div>
  <div class="col-links"><h4>Top Savings Accounts</h4><ul><li>Easy Access Accounts</li><li>Fixed Rate Bonds</li><li>Cash ISA Accounts</li><li>Notice Accounts</li></ul></div>
  <div class="col-links"><h4>&nbsp;</h4><ul><li>Rate Tracker</li><li>Savings Guides</li><li>Latest News</li></ul></div>
  <div class="col-links"><h4>&nbsp;</h4><ul><li>Our Awards</li><li>Meet the Team</li><li>Contact Us</li></ul></div>
  <div class="signup"><h4>Sign up for our newsletter</h4><p>Stay in the loop with the latest rates and tips delivered straight to your inbox.</p><div class="field">Your email address<span class="go">Join</span></div></div>
</footer>
<div class="bottom">Terms &amp; Conditions | Privacy Policy | Cookie Policy | Website Security<br>© Thrift Beacon 2015. All rights reserved.</div>
</body>
</html>
```